Business Card Design Project

This is the first time we use our new logo. We need a business card that we can use both on our institutional corporate relationships and also that works for our staff that deals with consumers directly.

VELUNDA is a new company dedicated to empower consumers and to provide them with the best choices for specialized health care using the latest telemedicine technology (medicine at a distance via videoconference).

We want to print this cards in high quality materials and process. We will like designs that allow us to use UV spot varnish and other techniques that will differentiate us.

We are including Two different versions of Color logos. In addition we are including white over black background logos. Those can be used replacing the black for a color.

Please note this is the first time we will be creating any corporate materials with our new logo and colors.

Target Market(s)

34+ consumers of medium high and high socioeconomic levels.

Industry/Entity Type

Health

Requirements
Must have
• Our logo on its original colors
Should not have
• Any other graphical element or design that is not our logo

```html
<!DOCTYPE html>
<html lang="en">
<head>
<meta charset="utf-8">
<title>VELUNDA Business Card</title>
<link rel="stylesheet" href="https://fonts.googleapis.com/css2?family=Open+Sans:wght@400;600;700&display=swap">
<style>
  :root {
    --backdrop: #8a8a8a;
    --card-blue: #1b75bb;
    --card-white: #ffffff;
    --brand-navy: #1d4f7a;
    --brand-teal: #14a59a;
    --title-blue: #1b5ea6;
    --ink: #4a4a4a;
    --ink-strong: #3f3f3f;
  }
  * { margin: 0; padding: 0; box-sizing: border-box; }
  html, body {
    width: 1200px;
    height: 1164px;
    overflow: hidden;
  }
  body {
    background: var(--backdrop);
    font-family: "Open Sans", Arial, sans-serif;
    position: relative;
  }
  .card {
    position: absolute;
    top: 215px;
    width: 419px;
    height: 735px;
  }
  .card--front {
    left: 164px;
    background: var(--card-blue);
  }
  .card--back {
    left: 617px;
    background: var(--card-white);
  }
  .front-mark {
    position: absolute;
    left: 0;
    right: 0;
    top: 250px;
    text-align: center;
    color: var(--card-white);
  }
  .front-mark__dot {
    display: block;
    width: 96px;
    height: 96px;
    margin: 0 auto 34px;
    border-radius: 50%;
    background: var(--card-white);
  }
  .front-mark__name {
    font-size: 46px;
    font-weight: 700;
    letter-spacing: 4px;
  }
  .back-mark {
    position: absolute;
    left: 0;
    right: 0;
    top: 70px;
    text-align: center;
  }
  .back-mark__dot {
    display: block;
    width: 72px;
    height: 72px;
    margin: 0 auto 46px;
    border-radius: 50%;
    background: var(--brand-teal);
  }
  .back-mark__name {
    color: var(--brand-navy);
    font-size: 52px;
    font-weight: 700;
    letter-spacing: 4px;
    line-height: 1;
  }
  .person {
    position: absolute;
    left: 48px;
    top: 344px;
  }
  .person__name {
    font-size: 20px;
    font-weight: 700;
    color: var(--ink-strong);
    word-spacing: 4px;
  }
  .person__title {
    font-size: 14px;
    color: var(--title-blue);
    margin-top: 2px;
  }
  .contact {
    position: absolute;
    left: 44px;
    top: 448px;
    list-style: none;
    font-size: 18px;
    line-height: 24.5px;
    color: var(--ink);
  }
  .address {
    position: absolute;
    left: 39px;
    top: 576px;
    width: 360px;
    font-size: 18px;
    line-height: 25px;
    color: var(--ink);
    font-style: normal;
  }
</style>
</head>
<body>
  <section class="card card--front" aria-label="Card front">
    <div class="front-mark">
      <span class="front-mark__dot"></span>
      <div class="front-mark__name">VELUNDA</div>
    </div>
  </section>

  <section class="card card--back" aria-label="Card back">
    <div class="back-mark">
      <span class="back-mark__dot"></span>
      <div class="back-mark__name">VELUNDA</div>
    </div>

    <div class="person">
      <div class="person__name">Mara Ostend</div>
      <div class="person__title">CEO</div>
    </div>

    <ul class="contact">
      <li>P: (000) 000-0000</li>
      <li>F: (000) 000-0000</li>
      <li>E: hello@velunda.com</li>
      <li>W: www.velunda.com</li>
    </ul>

    <address class="address">
      0000 Linden Rd. Suite 000 Marlowe,<br>
      TT 00000, 000 Linden Rd. Suite 000<br>
      Marlowe, NJ 000000
    </address>
  </section>
</body>
</html>
```